Bold Website Redesign for a Disruptive Training Brand

Brightmoor Labs is a bold, no-fluff sales & leadership training company powered by AI-driven practice and behavioral science. We’ve already built our website structure and copy in Craftly.io — now we need a designer to fully transform the visual design across all pages (Home, Approach, Programs, About, Contact).
We’re looking for a modern, memorable, high-performance aesthetic that blends human energy, science, and tech without feeling corporate or safe. Clean, bold typography, fluid layout, strong emotional hero moments, subtle motion, and imagery that mixes real people with abstract scientific/tech visuals.Because our clients are primarily North American, please ensure any human photography or AI-generated imagery reflects a North American business context and demographics (modern, diverse, and realistic).

Your job is visual redesign only — no coding required.
The final design must be practical to rebuild inside Craftly.io.

A full, detailed creative brief (plus logo files) is included in the uploaded files.
If you can bring a mix of edge, intelligence, and strong visual storytelling, we’d love to see your work.

Website is already built in Craftly.io at - https://brightmoor-website-tempdesign.craftly.app — structure is set, visuals need redesign.

```html
<!DOCTYPE html>
<html lang="en">
<head>
<meta charset="utf-8">
<title>Brightmoor Labs — Training that Practices Back</title>
<link href="https://fonts.googleapis.com/css2?family=Poppins:wght@400;500;600;700&display=swap" rel="stylesheet">
<style>
:root{
  --navy:#0f1d3a;
  --ink:#1c2233;
  --blue:#2f6fd0;
  --blue-deep:#2a4fa8;
  --sky:#43c3f0;
  --cyan:#3fb8ec;
  --pale:#e6effb;
  --white:#ffffff;
  --muted:#3c4456;
}
*{box-sizing:border-box;margin:0;padding:0}
html,body{width:1200px;height:3947px;overflow:hidden}
body{font-family:"Poppins",sans-serif;color:var(--ink);background:var(--white);position:relative}
.abs{position:absolute}
.btn{position:absolute;display:flex;align-items:center;justify-content:center;border-radius:30px;font-weight:600;font-size:13px;text-transform:uppercase;color:var(--white);letter-spacing:.2px}
.btn-solid{background:linear-gradient(90deg,var(--blue-deep),var(--cyan))}
.btn-sky{background:var(--sky)}
.btn-line{border:2px solid var(--white)}
.brand{font-weight:600;color:var(--white);letter-spacing:3px;font-size:18px;display:flex;align-items:center;gap:12px}
.brand .dot{width:46px;height:46px;border-radius:50%;border:2px solid var(--white)}

/* hero */
.hero{position:absolute;left:0;top:0;width:1200px;height:720px;background:linear-gradient(100deg,#3d7fd6 0%,#3b69bf 40%,#243e7a 100%)}
.hero-photo{position:absolute;left:520px;top:0;width:680px;height:700px;background:linear-gradient(120deg,rgba(70,120,200,.0),#2b3d64 60%,#1b2544)}
.nav{position:absolute;top:34px;left:458px;display:flex;gap:48px;font-size:13px;font-weight:500;color:var(--white)}
.nav .active{position:relative}
.nav .active::before{content:"";position:absolute;left:-4px;right:-4px;top:-34px;height:4px;background:var(--white)}
.hero h1{position:absolute;left:122px;top:190px;font-size:56px;line-height:66px;color:var(--white);font-weight:700}
.hero .lead{position:absolute;left:128px;top:338px;width:380px;font-size:20px;line-height:28px;font-weight:600;color:var(--white)}
.hero .sub{position:absolute;left:128px;top:406px;width:380px;font-size:13.5px;line-height:19px;color:var(--white)}

/* problem */
.problem-h{position:absolute;left:0;width:1200px;top:800px;text-align:center;font-size:43px;line-height:52px;font-weight:600;color:var(--ink)}
.grad-text{background:linear-gradient(90deg,var(--blue-deep),var(--sky));-webkit-background-clip:text;background-clip:text;color:transparent}
.problem-p{position:absolute;left:170px;width:860px;top:920px;text-align:center;font-size:19px;line-height:35px;color:var(--muted)}

/* practice */
.practice{position:absolute;left:0;top:1700px;width:1200px;height:680px;background:linear-gradient(180deg,#e9f1fc,#d6e6fa 70%,#c8def8)}
.practice h2{position:absolute;left:132px;top:65px;font-size:40px;line-height:48px;font-weight:700;color:var(--ink)}
.practice .intro{position:absolute;left:578px;top:80px;width:450px;font-size:19px;line-height:27px}
.step{position:absolute;width:290px;height:290px;border-radius:50%;background:var(--white);display:flex;flex-direction:column;align-items:center;justify-content:center;text-align:center;padding:0 36px}
.step h3{font-size:17px;font-weight:500;margin:14px 0 8px;letter-spacing:.5px}
.step p{font-size:13px;line-height:16px}
.step.featured{background:linear-gradient(135deg,#2f5bb8,#3fb0ea);color:var(--white)}
.icon{width:62px;height:62px}

/* team */
.team h2{position:absolute;left:134px;top:2545px;font-size:38px;line-height:56px;font-weight:600}
.team p{position:absolute;left:134px;top:2670px;width:500px;font-size:20px;line-height:34px;color:var(--muted)}

/* cta */
.cta{position:absolute;left:108px;top:3093px;width:967px;height:464px;border-radius:14px;background:linear-gradient(110deg,#3260c0 0%,#3a86d8 55%,#47c8f2 100%);text-align:center;color:var(--white);z-index:2}
.cta .mark{margin-top:90px;font-size:18px;font-weight:600;letter-spacing:3px}
.cta h2{margin-top:14px;font-size:42px;line-height:50px;font-weight:700}
.footer{position:absolute;left:0;top:3480px;width:1200px;height:467px;background:linear-gradient(180deg,#11203f,#0d1a33)}
.footer h4{font-size:14px;font-weight:600;color:var(--white);margin-bottom:18px;letter-spacing:.3px}
.footer .col{position:absolute;top:180px;color:var(--white);font-size:13px}
.footer ul{list-style:none}
.footer li{margin-bottom:13px}
.contact-row{display:flex;gap:12px;align-items:flex-start;margin-bottom:20px}
.social{display:flex;gap:8px}
.social span{width:30px;height:30px;border-radius:50%;background:var(--white)}
</style>
</head>
<body>

<!-- HERO -->
<section class="hero">
  <div class="hero-photo" role="img" aria-label="Photo of three colleagues gathered around a screen reviewing data"></div>
  <svg class="abs" style="left:0;top:620px" width="1200" height="100" viewBox="0 0 1200 100"><path d="M0 75 C150 40 300 30 450 45 C650 65 750 5 1000 25 C1100 33 1160 60 1200 65 L1200 100 L0 100Z" fill="#fff"/></svg>
  <div class="brand abs" style="left:122px;top:24px">BRIGHTMOOR LABS</div>
  <nav class="nav"><span class="active">HOME</span><span>APPROACH</span><span>PROGRAMS</span><span>ABOUT</span><span>CONTACT</span></nav>
  <div class="btn btn-sky" style="left:1004px;top:28px;width:128px;height:36px;font-size:11px">Lets Talk</div>
  <h1>Training that<br>Practices Back</h1>
  <p class="lead">AI-driven sustainment that builds mastery — so you don't have to.</p>
  <p class="sub">You'll see measurable growth as your people turn insight into habit — automatically, sustainably, and without extra work for their leaders.</p>
  <div class="btn btn-sky" style="left:127px;top:495px;width:196px;height:46px">See how we do it</div>
  <div class="btn btn-line" style="left:340px;top:493px;width:195px;height:47px">Lets Talk</div>
</section>

<!-- PROBLEM -->
<h2 class="problem-h">The real problem isn't your people<br><span class="grad-text">it's the forgetting curve.</span></h2>
<p class="problem-p">Within a week, most training disappears. Leaders are left guessing who's using what they learned — and no one has time to fix it. We built Brightmoor Labs to make progress automatic, measurable, and real.</p>
<div class="btn btn-solid" style="left:505px;top:1050px;width:195px;height:47px">See how we do it</div>

<div class="abs" style="left:75px;top:1130px;width:450px;height:480px;border-radius:50%;background:radial-gradient(circle,#f3f5fb 55%,#d9e6f6 85%,#e4dcf2);border:3px solid #bfe6f6" role="img" aria-label="Photo of a smiling man in a light suit using a tablet"></div>
<svg class="abs" style="left:510px;top:1230px" width="150" height="300" viewBox="0 0 150 300"><g fill="none" stroke="#9fd2ee" stroke-width="5"><path d="M0 145 C60 145 80 0 145 10"/><path d="M0 145 H145"/><path d="M0 145 C60 145 80 290 145 280"/></g></svg>
<svg class="abs" style="left:650px;top:1195px" width="466" height="353" viewBox="0 0 466 353">
  <defs><clipPath id="card"><rect width="466" height="353" rx="12"/></clipPath>
  <linearGradient id="area" x1="0" y1="0" x2="1" y2="1"><stop offset="0" stop-color="#2b63c4"/><stop offset="1" stop-color="#46b8ec"/></linearGradient></defs>
  <g clip-path="url(#card)">
    <rect width="466" height="353" fill="#fff"/>
    <g stroke="#e4e9f3" stroke-width="1">
      <path d="M0 30H466M0 60H466M0 90H466M0 120H466M0 150H466M0 180H466M0 210H466M0 240H466M0 270H466M0 300H466M0 330H466"/>
      <path d="M30 0V353M60 0V353M90 0V353M120 0V353M150 0V353M180 0V353M210 0V353M240 0V353M270 0V353M300 0V353M330 0V353M360 0V353M390 0V353M420 0V353M450 0V353"/>
    </g>
    <polyline points="0,140 55,140 135,130 185,155 310,165 400,155 466,175" fill="none" stroke="#a9bde0" stroke-width="2"/>
    <g fill="#2f6fd0"><circle cx="55" cy="140" r="5"/><circle cx="185" cy="155" r="5"/><circle cx="307" cy="165" r="5"/><circle cx="399" cy="160" r="5"/></g>
    <path d="M0 160 C60 220 160 245 300 250 C380 252 430 255 466 258 V353 H0Z" fill="url(#area)"/>
    <path d="M0 160 C60 220 160 245 300 250 C380 252 430 255 466 258" fill="none" stroke="#fff" stroke-width="4"/>
  </g>
  <g font-family="Poppins,sans-serif" font-weight="600" font-size="11" fill="#1c2233">
    <text x="36" y="94">PEOPLE</text><text x="20" y="108">FORGET FAST</text>
    <text x="260" y="190">WITHIN A WEEK,</text><text x="272" y="204">70% IS GONE</text>
    <text x="318" y="292" fill="#fff">WE BUILT THE FIX IN</text>
  </g>
</svg>

<!-- PRACTICE -->
<section class="practice">
  <svg class="abs" style="left:0;top:600px" width="1200" height="80" viewBox="0 0 1200 80"><path d="M0 40 C150 70 280 70 420 40 C560 10 700 10 830 30 C980 55 1100 40 1200 25 L1200 80 L0 80Z" fill="#fff"/></svg>
  <h2>Practice Made<br><span class="grad-text">Permanent.</span></h2>
  <p class="intro">You'll replace "hope they remember" with a system that makes sure they do.</p>
  <svg class="abs" style="left:110px;top:210px" width="980" height="330" viewBox="0 0 980 330" fill="none" stroke="#2f5bb8" stroke-width="3">
    <path d="M13 105 C10 230 100 310 172 310 C260 310 330 240 330 160 C330 60 400 5 501 5 C600 5 672 60 672 160 C672 240 740 310 828 310 C900 310 968 240 968 100"/>
    <circle cx="13" cy="102" r="6" fill="#fff"/><circle cx="968" cy="96" r="6" fill="#fff"/>
  </svg>
  <div class="step" style="left:137px;top:227px">
    <svg class="icon" viewBox="0 0 60 60" fill="none" stroke="#2f5bb8" stroke-width="2"><path d="M30 10c-8-4-18 2-17 10-6 3-6 12 0 15-1 8 8 13 17 9z"/><path d="M30 10v34M30 20h12M30 30h18M30 40h12"/><circle cx="44" cy="20" r="2.5"/><circle cx="50" cy="30" r="2.5"/><circle cx="44" cy="40" r="2.5"/></svg>
    <h3>LEARN</h3><p>Fast, focused workshops, built on science, that install the mindset and skills that matter most.</p>
  </div>
  <div class="step featured" style="left:465px;top:222px">
    <svg class="icon" viewBox="0 0 60 60" fill="none" stroke="#fff" stroke-width="2"><circle cx="30" cy="30" r="18"/><path d="M12 30h36M30 12v36M17 17l26 26M43 17L17 43"/><circle cx="30" cy="30" r="8"/></svg>
    <h3>CERTIFY</h3><p>Programmatic AI-driven practice and feedback - mastery without management overhead.</p>
  </div>
  <div class="step" style="left:785px;top:227px">
    <svg class="icon" viewBox="0 0 60 60" fill="none" stroke="#2f5bb8" stroke-width="2"><rect x="14" y="10" width="38" height="30" rx="2"/><path d="M34 36V26M40 36V20M46 36V24M18 28l6-6 6 4 8-10"/><circle cx="14" cy="44" r="8"/><path d="M14 36v8h8"/></svg>
    <h3>SUSTAIN</h3><p>Light-touch challenges and dashboards that keep skills sharp long after training ends.</p>
  </div>
</section>

<!-- TEAM -->
<section class="team">
  <h2>Built by people who've led<br><span class="grad-text">the change themselves.</span></h2>
  <p>Behind Brightmoor Labs are leaders who've lived the challenge of making learning last. They've scaled companies, built cultures, and led transformation — and now they've designed the system they always wished existed.</p>
  <div class="btn btn-solid" style="left:139px;top:2868px;width:212px;height:50px;font-size:14px">Meet the team</div>
  <div class="abs" style="left:665px;top:2395px;width:660px;height:650px;border-radius:50%;border:3px solid #4fa6e6"></div>
  <div class="abs" style="left:678px;top:2408px;width:634px;height:624px;border-radius:50%;background:linear-gradient(135deg,#c9d6e6,#6f7f93 55%,#3b4657)" role="img" aria-label="Photo of two colleagues smiling at a tablet together"></div>
  <div class="abs" style="left:647px;top:2815px;width:136px;height:136px;border-radius:50%;background:#fff;display:flex;align-items:center;justify-content:center;font-weight:600;font-size:14px;color:var(--blue-deep)">Brightmoor</div>
</section>

<!-- CTA + FOOTER -->
<footer class="footer">
  <div class="brand abs" style="left:106px;top:170px">BRIGHTMOOR LABS</div>
  <p class="abs" style="left:119px;top:248px;width:290px;color:#fff;font-size:12px;line-height:19px">Making learning that sticks through AI-driven sustainment and behavioral science.</p>
  <p class="abs" style="left:119px;top:317px;color:#fff;font-size:11px">© 2024 Brightmoor Labs. All rights reserved.</p>
  <div class="col" style="left:491px"><h4>NAVIGATION</h4><ul><li>Home</li><li>Approach</li><li>Programs</li><li>About</li><li>Contact</li></ul></div>
  <div class="col" style="left:671px"><h4>CONTACT US</h4>
    <div class="contact-row"><svg width="18" height="14" viewBox="0 0 18 14" fill="none" stroke="#fff" stroke-width="1.6"><rect x="1" y="1" width="16" height="12"/><path d="M1 1l8 7 8-7"/></svg>contact@brightmoorlabs.com</div>
    <div class="contact-row"><svg width="16" height="16" viewBox="0 0 16 16" fill="#fff"><path d="M3 1l3 3-2 2c1 2 3 4 5 5l2-2 3 3-2 3C7 14 2 9 1 3z"/></svg>+1 (555) 014-2870</div>
    <div class="contact-row"><svg width="14" height="18" viewBox="0 0 14 18" fill="#fff"><path d="M7 0a7 7 0 0 0-7 7c0 5 7 11 7 11s7-6 7-11a7 7 0 0 0-7-7zm0 10a3 3 0 1 1 0-6 3 3 0 0 1 0 6z"/></svg><span>4820 Canyon Ridge Rd Suite 210<br>Phoenix, AZ 85016</span></div>
  </div>
  <div class="col" style="left:939px;top:175px"><h4>FOLLOW US</h4><div class="social"><span></span><span></span><span></span></div></div>
</footer>

<section class="cta">
  <div class="mark">BRIGHTMOOR LABS</div>
  <h2>Ready to see what lasting<br>Capability looks like?</h2>
  <div class="btn btn-line" style="left:364px;top:268px;width:230px;height:55px;font-size:15px;text-transform:none">Start a Conversion</div>
</section>

</body>
</html>
```